Business Card Design for Occupational Medicine Start Up Company

We need to design a professional business card. We are a healthcare company providing occupational medicine services to blue collar industries. We are professional, efficient and high quality service providers.

Target Market(s)

Blue Collar Industry: Shipbuilding, Ports, Trucking Companies; The Executives and Safety Officers for these companies

Industry/Entity Type

Healthcare

Contact Information for Business Card

Logo, Name, Title, Email, Phone

Other font styles liked:
• Please match our Brand Guide

Requirements
Must have
• Our Company Colors and Logo

```html
<!DOCTYPE html>
<html lang="en">
<head>
<meta charset="utf-8">
<title>Dockside Care Clinics – Business Card</title>
<link href="https://fonts.googleapis.com/css2?family=Montserrat:wght@400;500;600;700;800&display=swap" rel="stylesheet">
<style>
  :root {
    --sky: #23a9e1;
    --navy: #2b3990;
    --amber: #f9b04b;
    --ink: #1a1a1a;
    --paper: #ffffff;
    --edge: #cfcfcf;
  }
  * { box-sizing: border-box; margin: 0; padding: 0; }
  html, body {
    width: 1200px;
    height: 1200px;
    overflow: hidden;
    background: var(--paper);
    font-family: "Montserrat", sans-serif;
  }
  .sheet {
    position: relative;
    width: 1200px;
    height: 1200px;
  }
  .card {
    position: absolute;
    top: 452px;
    width: 516px;
    height: 295px;
  }
  .card--front {
    left: 64px;
    background: var(--paper);
    border: 1px solid var(--edge);
  }
  .card--back {
    left: 620px;
    background: var(--sky);
  }

  /* front stripes */
  .stripe {
    position: absolute;
    top: 0;
    bottom: 0;
    width: 12px;
  }
  .stripe--sky { left: 22px; background: var(--sky); }
  .stripe--navy { left: 44px; background: var(--navy); }
  .stripe--amber { left: 66px; background: var(--amber); }

  /* brand lockup */
  .brand {
    position: absolute;
    display: flex;
    align-items: center;
    gap: 14px;
  }
  .brand__dot {
    width: 52px;
    height: 52px;
    border-radius: 50%;
    flex: none;
  }
  .brand__name {
    font-weight: 700;
    line-height: 1.15;
    text-transform: uppercase;
  }
  .brand__name span { display: block; }
  .brand__sub {
    font-size: 0.5em;
    letter-spacing: 0.32em;
    text-align: center;
  }

  .card--front .brand { left: 112px; top: 34px; }
  .card--front .brand__dot { background: var(--navy); }
  .card--front .brand__name { color: var(--navy); font-size: 22px; }

  .card--back .brand {
    left: 0;
    right: 0;
    top: 78px;
    flex-direction: column;
    gap: 18px;
  }
  .card--back .brand__dot {
    width: 74px;
    height: 74px;
    background: var(--paper);
  }
  .card--back .brand__name { color: var(--paper); font-size: 28px; text-align: center; }

  /* person block */
  .person {
    position: absolute;
    left: 112px;
    top: 166px;
    color: var(--ink);
  }
  .person__name {
    font-size: 30px;
    font-weight: 400;
    line-height: 1;
  }
  .person__name strong { font-weight: 800; }
  .person__title {
    font-size: 14.5px;
    font-weight: 400;
    margin-top: 3px;
  }

  .contact {
    position: absolute;
    left: 112px;
    top: 229px;
    list-style: none;
    color: var(--ink);
    font-size: 15.5px;
  }
  .contact__item {
    display: flex;
    align-items: center;
    gap: 6px;
    height: 20px;
  }
  .contact__item strong { font-weight: 700; }
  .contact__icon { width: 11px; height: 11px; flex: none; }
</style>
</head>
<body>
<main class="sheet">

  <section class="card card--front" aria-label="Business card front">
    <div class="stripe stripe--sky"></div>
    <div class="stripe stripe--navy"></div>
    <div class="stripe stripe--amber"></div>

    <div class="brand">
      <div class="brand__dot"></div>
      <div class="brand__name">
        <span>Dockside Care</span>
        <span class="brand__sub">Clinics</span>
      </div>
    </div>

    <div class="person">
      <h1 class="person__name"><strong>Dana</strong> Whitlock</h1>
      <p class="person__title">Managing Director</p>
    </div>

    <ul class="contact">
      <li class="contact__item">
        <svg class="contact__icon" viewBox="0 0 11 11" aria-hidden="true">
          <rect width="11" height="11" fill="#2b3990"/>
          <rect x="2.3" y="3.3" width="6.4" height="4.4" fill="none" stroke="#fff" stroke-width="0.8"/>
          <polyline points="2.3,3.3 5.5,5.8 8.7,3.3" fill="none" stroke="#fff" stroke-width="0.8"/>
        </svg>
        dana@docksidecare.com
      </li>
      <li class="contact__item">
        <svg class="contact__icon" viewBox="0 0 11 11" aria-hidden="true">
          <rect width="11" height="11" fill="#2b3990"/>
          <path d="M3 2.5 L4.4 2.5 L4.9 4.2 L4.1 4.9 Q4.9 6.4 6.2 7 L6.9 6.2 L8.5 6.7 L8.5 8.1 Q5.5 8.4 3.8 6.3 Q2.6 4.7 3 2.5 Z" fill="#fff"/>
        </svg>
        <span>www.<strong>docksidecare</strong>.com</span>
      </li>
    </ul>
  </section>

  <section class="card card--back" aria-label="Business card back">
    <div class="brand">
      <div class="brand__dot"></div>
      <div class="brand__name">
        <span>Dockside Care</span>
        <span class="brand__sub">Clinics</span>
      </div>
    </div>
  </section>

</main>
</body>
</html>
```